Modern Minimal Acne Clearing Set Retail Box

We need a design for our slide out packaging box. The packaging is for our Acne Clearing Set, which includes a cleanser and a cream. We would love something that's original,minimal and modern and not gender specific. Feel free to use your own take on design. Surprise us. I've attached dimensions of the box as well as some refrence images of some boxes we like. It doesn't have to be exactly like these images but its a good starting point. Ive also attached our logo (you can change the logo style if needed to fit your design), your free to use other fonts and colors to match your design. The back of the box will have the drug fact for both products.

Target Market(s)

Everybody

Industry/Entity Type

Beauty

Font styles to use
Sans Serif

Colors
3176b5
33a6d7
85cae6
33b8a4
86cfc6
1b1b1b
ececec

Requirements
Must have
• Originality

```html
<!DOCTYPE html>
<html lang="en">
<head>
<meta charset="utf-8">
<title>Acne Clearing Set – Retail Box Front</title>
<link rel="stylesheet" href="https://fonts.googleapis.com/css2?family=Cabin:wght@400;500&display=swap">
<style>
  :root {
    --backdrop: #ececec;
    --box-face: #ffffff;
    --ink: #1b1b1b;
    --label-grey: #4a4a4a;
    --sky: #7dbde3;
    --sky-pale: #d6ecf8;
    --silver-dark: #5e6468;
    --silver-light: #ffffff;
  }
  * { margin: 0; padding: 0; box-sizing: border-box; }
  html, body {
    width: 1200px;
    height: 1200px;
    overflow: hidden;
    background: var(--backdrop);
    font-family: "Cabin", "Gill Sans", sans-serif;
  }
  .canvas {
    position: relative;
    width: 1200px;
    height: 1200px;
  }
  .box-front {
    position: absolute;
    left: 372px;
    top: 79px;
    width: 455px;
    height: 985px;
    background: var(--box-face);
  }
  .brand-name {
    position: absolute;
    left: 0;
    right: 0;
    top: 266px;
    line-height: 60px;
    text-align: center;
    font-size: 52px;
    font-weight: 500;
    letter-spacing: 1px;
    color: var(--ink);
  }
  .brand-mark {
    position: absolute;
    left: 167px;
    top: 548px;
    width: 120px;
    height: 120px;
    border-radius: 50%;
    background: radial-gradient(circle, var(--box-face) 0 18%, var(--sky-pale) 40%, var(--sky) 72%, var(--box-face) 100%);
  }
  .product-title {
    position: absolute;
    left: 0;
    right: 0;
    top: 724px;
    line-height: 28px;
    text-align: center;
    font-size: 23px;
    font-weight: 400;
    letter-spacing: 1.5px;
    color: var(--label-grey);
  }
  .product-contents {
    position: absolute;
    left: 0;
    right: 0;
    top: 762px;
    line-height: 24px;
    text-align: center;
    font-size: 20px;
    font-weight: 400;
    letter-spacing: 0.5px;
    color: var(--label-grey);
  }
  .silver-band {
    position: absolute;
    left: 0;
    right: 0;
    top: 824px;
    height: 11px;
    background: linear-gradient(90deg, var(--silver-dark) 0%, #a9aeb1 30%, var(--silver-light) 52%, #a9aeb1 72%, var(--silver-dark) 100%);
  }
  .sky-band {
    position: absolute;
    left: 0;
    right: 0;
    top: 844px;
    height: 40px;
    background: var(--sky);
  }
</style>
</head>
<body>
  <main class="canvas">
    <section class="box-front">
      <div class="brand-name">Solvea Skin</div>
      <div class="brand-mark" role="img" aria-label="Light blue radiating sunburst emblem"></div>
      <h1 class="product-title">ACNE CLEARING SET</h1>
      <p class="product-contents">cleanser &amp; cream</p>
      <div class="silver-band"></div>
      <div class="sky-band"></div>
    </section>
  </main>
</body>
</html>
```